Heartnight Soiree- The Velvet Evening

This is an elegant Dinner concert event for Valentines day February 14 2020 in Vancouver WA. Live R&B band.

Join us for an Evening of live R&B music Featuring some of Oregon and Washington's talented music artists

Tickets prices: $30 concert only pp
$60 dinner and concert pp
$90 VIP Dinner & one drink/Concert/Premium Seating/Special Gift pp
Doors open @ 6:45 Event is 7:30 to 10:30
Location: Lanternfly
417 Hollis St.B Vancouver, WA 98662

www.thekestrelhouse.example for more info.

Target Market(s)

Adults /Couples

Industry/Entity Type

Entertainment Industry

Font styles to use
Sans Serif
Decorative

Colors

Designer to choose colors to be used in the design.

Requirements
Must have
• Add the logos for Sponsors of the Event. Marlows is the main sponsor of the event.
• Main colors should be Red and right for valentine. Needs to be sized for a 5x7 Flyer
• Include the pictures of the Music Artists

```html
<!DOCTYPE html>
<html lang="en">
<head>
<meta charset="utf-8">
<title>Heartnight Soiree – The Velvet Evening</title>
<link href="https://fonts.googleapis.com/css2?family=Great+Vibes&family=Alegreya:ital,wght@0,400;0,700;1,400&family=Fira+Sans+Condensed:wght@400;600&family=Open+Sans:ital,wght@0,400;1,400&display=swap" rel="stylesheet">
<style>
  :root {
    --red-deep: #8e0c16;
    --red-mid: #c3151f;
    --red-bright: #e2262e;
    --white: #ffffff;
    --gold: #ffd54a;
    --black: #000000;
    --photo-a: #3a5a8a;
    --photo-b: #5a2a1e;
    --photo-c: #2a1c1c;
    --frame: #f4b9bd;
  }
  * { margin: 0; padding: 0; box-sizing: border-box; }
  html, body { width: 857px; height: 1200px; overflow: hidden; }
  body { background: var(--red-deep); }
  .flyer {
    position: relative;
    width: 857px; height: 1200px; overflow: hidden;
    background:
      radial-gradient(ellipse at 55% 45%, var(--red-bright) 0%, var(--red-mid) 40%, var(--red-deep) 100%);
    color: var(--white);
    font-family: "Alegreya", Georgia, serif;
  }
  .backdrop { position: absolute; inset: 0; }
  .headline {
    position: absolute; top: 8px; left: 0; width: 100%;
    text-align: center;
    font-family: "Great Vibes", cursive; font-weight: 400;
    font-size: 124px; line-height: 1.2;
    transform: rotate(-3deg);
  }
  .intro {
    position: absolute; top: 196px; left: 0; width: 100%;
    text-align: center; font-size: 28px; line-height: 33.5px;
  }
  .artists { position: absolute; left: 0; top: 340px; overflow: visible; }
  .venue { position: absolute; top: 372px; left: 449px; }
  .venue-name { font-weight: 700; font-size: 24px; letter-spacing: 0.5px; }
  .venue-address {
    margin-top: 12px;
    font-family: "Fira Sans Condensed", sans-serif; font-size: 23px; line-height: 32px;
  }
  .venue-times {
    margin-top: 18px; color: var(--white);
    font-family: "Fira Sans Condensed", sans-serif; font-weight: 600; font-size: 25px; line-height: 32px;
  }
  .tickets {
    position: absolute; top: 765px; left: 0; width: 100%;
    text-align: center;
  }
  .tickets-title { font-weight: 700; font-size: 20px; letter-spacing: 2.5px; margin-left: -24px; }
  .ticket-list {
    list-style: none; margin-top: 14px;
    font-family: "Open Sans", sans-serif; font-size: 21.5px; line-height: 32px;
  }
  .ticket-list sup { font-size: 12px; line-height: 0; vertical-align: 9px; }
  .ticket-list .note { font-style: italic; }
  .sponsor {
    position: absolute; display: flex; align-items: center; justify-content: center; gap: 12px;
    font-family: "Alegreya", Georgia, serif; font-weight: 700;
  }
  .sponsor-main { left: 40px; top: 955px; width: 343px; height: 141px; background: var(--black); color: var(--gold); font-size: 34px; letter-spacing: 2px; }
  .sponsor-main .mark { width: 34px; height: 34px; background: var(--gold); }
  .sponsor-salon { left: 402px; top: 990px; width: 199px; height: 98px; background: var(--white); color: var(--black); font-size: 19px; font-weight: 400; }
  .sponsor-cheer { left: 620px; top: 990px; width: 198px; height: 98px; background: var(--black); color: var(--white); font-size: 22px; }
  .sponsor-cheer .mark { width: 22px; height: 22px; border-radius: 50%; background: var(--white); }
  .more-info {
    position: absolute; top: 1136px; left: 0; width: 100%;
    text-align: center; font-size: 24px; letter-spacing: 0.5px;
  }
</style>
</head>
<body>
<main class="flyer">
  <div class="backdrop" role="img" aria-label="Soft blurred red hearts, ribbons and confetti scattered across the background"></div>

  <h1 class="headline">Join us</h1>

  <p class="intro">for an Evening of live R&amp;B music<br>Featuring some of<br>Oregon &amp; Washington's<br>talented music artists</p>

  <svg class="artists" width="560" height="480" viewBox="0 0 560 480" aria-label="Artist photos">
    <defs>
      <path id="heart" d="M0,-70 C-20,-120 -130,-110 -125,-30 C-120,40 -30,70 0,120 C30,70 120,40 125,-30 C130,-110 20,-120 0,-70 Z"/>
    </defs>
    <g transform="translate(226,123)" role="img" aria-label="Photo of a male R&amp;B singer in a cap">
      <use href="#heart" fill="var(--photo-a)" stroke="var(--frame)" stroke-width="8"/>
    </g>
    <g transform="translate(150,337) scale(0.97)" role="img" aria-label="Photo of a female R&amp;B singer with curly hair">
      <use href="#heart" fill="var(--photo-b)" stroke="var(--frame)" stroke-width="8"/>
    </g>
    <g transform="translate(397,307) scale(0.97)" role="img" aria-label="Photo of a female R&amp;B singer with red curly hair">
      <use href="#heart" fill="var(--photo-c)" stroke="var(--frame)" stroke-width="8"/>
    </g>
  </svg>

  <section class="venue">
    <h2 class="venue-name">LANTERNFLY</h2>
    <p class="venue-address">417 Hollis St.<br>B Vancouver, WA 98662</p>
    <p class="venue-times">Doors open @ 6:45<br>Event is 7:30 PM to 10:30 PM</p>
  </section>

  <section class="tickets">
    <h3 class="tickets-title">TICKETS PRICES</h3>
    <ul class="ticket-list">
      <li><sup>$</sup>30 concert only pp</li>
      <li><sup>$</sup>60 dinner and concert pp</li>
      <li><sup>$</sup>90 VIP Dinner &amp; one drink</li>
      <li class="note">Concert/Premium Seating/Special Gift pp</li>
    </ul>
  </section>

  <div class="sponsor sponsor-main"><span class="mark"></span>MARLOWS</div>
  <div class="sponsor sponsor-salon">The Amberly Salon</div>
  <div class="sponsor sponsor-cheer"><span class="mark"></span>CHEERWELL</div>

  <p class="more-info">For more info visit www.thekestrelhouse.example</p>
</main>
</body>
</html>
```